Design für einen Jahresplaner gesucht
Zielgruppe
Scannen und Designen Zahntechnischer und Zahnmedizinischer Arbeiten und das Fräsen und 3d Drucken von bereits in CAD konstruierten Objekten. Wir verfügen über die modernsten Zahntechnischen Technologien und bieten diese als Dienstleister für Dentallabore an.
Aufgabenstellung
Wir benotigen ein Jahresplaner für unsere Kunden. Die Beigefügte Vorlage dient regelrecht nur der Grösenvorlage.
Das Design soll Technisch und Innovativ sein. Gleischzeitig aber gradlinig und nicht zu verspielt.
Das Logo kann ruhig stark ins Auge fallen. Die Schriftfarben sollen überwigen dunkelgrau sein. Hervorzuhebende Bereiche wie z. B. Sonntage, Feiertage sollten die Logofaben beinhalten. Bilder können auch verwendet werden aber wir würden uns über ein Schönes Layout ohne Bilder auch freuen.
PS: Unter dem Logo muss in Feiner Schrift stehen
eine Marke der Norvak GmbH

```html
<!DOCTYPE html>
<html lang="de">
<head>
<meta charset="utf-8">
<title>Jahresplaner 2019</title>
<link href="https://fonts.googleapis.com/css2?family=Jost:wght@400;500;600&family=Arimo:wght@400;700&display=swap" rel="stylesheet">
<style>
:root{
  --stage:#f2f2f2;
  --ink:#3a3a3c;
  --pink:#e2297f;
  --blue:#29a8e0;
  --night:#1c1c1e;
  --pill:#3b3b3e;
  --paper:#e9eaec;
  --logo-grey:#5b5b5e;
  --accent:#f39200;
}
*{margin:0;padding:0;box-sizing:border-box}
html,body{width:1200px;height:1200px;overflow:hidden;background:var(--stage)}
.planner{position:absolute;left:20px;top:195px;width:1160px;height:809px;background:var(--paper);overflow:hidden;font-family:"Jost",sans-serif;color:var(--ink)}
.header{position:absolute;left:0;top:0;width:1160px;height:150px;background:var(--night)}
.header svg{position:absolute;left:0;top:0}
.contact{position:absolute;left:58px;top:42px;list-style:none;font-family:"Arimo",sans-serif;color:#fff;font-size:16px}
.contact li{display:flex;align-items:center;height:23px;margin-bottom:13px;padding-left:14px;background:var(--pill);white-space:nowrap;clip-path:polygon(0 0,95% 0,100% 100%,4% 100%)}
.contact li svg{position:static;margin-right:12px;flex:none}
.contact .c1{width:179px}.contact .c2{width:187px}.contact .c3{width:179px}
.year{position:absolute;left:521px;top:100px;font-family:"Arimo",sans-serif;font-weight:700;font-size:38px;color:#fff;letter-spacing:.5px}
.brand{position:absolute;left:883px;top:39px;width:277px;height:90px;background:#f4f4f4;clip-path:polygon(14% 0,100% 0,100% 100%,0 100%);display:flex;align-items:center;padding-left:52px;gap:10px}
.brand-dot{width:34px;height:34px;border-radius:50%;background:var(--accent)}
.brand-name{font-family:"Jost",sans-serif;font-weight:600;font-size:28px;color:var(--logo-grey);letter-spacing:.5px}
.month-bar{position:absolute;left:0;top:150px;width:1160px;height:21px;background:var(--blue)}
.month-bar span{position:absolute;top:2px;color:#fff;font-size:12px;font-weight:400}
.months{position:absolute;left:37px;top:184px;display:grid;grid-template-columns:repeat(13,82px)}
.month{position:relative}
.month ol{list-style:none}
.month li{height:18.5px;display:flex;align-items:center;font-size:9.5px}
.month li b{font-weight:400;width:18px;flex:none}
.month li s{text-decoration:none;width:22px;flex:none}
.month li i{font-style:normal;font-size:4.6px;line-height:1.15;width:36px;overflow-wrap:break-word}
.month li.h b,.month li.h s{color:var(--pink)}
.foot{position:absolute;top:575px;left:0;width:78px;font-size:4.2px;line-height:1.3}
.bottom-strip{position:absolute;left:0;bottom:0;width:1160px;height:11px;background:#2e3033}
</style>
</head>
<body>
<div class="planner">
  <header class="header">
    <svg width="1160" height="150" viewBox="0 0 1160 150">
      <defs>
        <linearGradient id="bridgeTone" x1="0" y1="0" x2="1" y2="1">
          <stop offset="0" stop-color="#2a2a2c"/>
          <stop offset=".45" stop-color="#9a9a9c"/>
          <stop offset="1" stop-color="#3a3a3c"/>
        </linearGradient>
      </defs>
      <polygon points="557,0 1160,0 1160,150 635,150" fill="url(#bridgeTone)" role="img" aria-label="Foto einer gefrästen Zahnbrücke auf Implantaten"/>
      <polygon points="252,0 256,0 317,150 313,150" fill="var(--blue)"/>
      <polygon points="557,0 562,0 640,150 635,150" fill="var(--blue)"/>
      <g fill="#2b2b2d" stroke="#6a6a6c" stroke-width="2">
        <rect x="-25" y="-25" width="50" height="50" rx="6" transform="translate(339,61) rotate(45)"/>
        <rect x="-25" y="-25" width="50" height="50" rx="6" transform="translate(432,55) rotate(45)"/>
        <rect x="-25" y="-25" width="50" height="50" rx="6" transform="translate(526,61) rotate(45)"/>
        <rect x="-25" y="-25" width="50" height="50" rx="6" transform="translate(387,106) rotate(45)"/>
        <rect x="-25" y="-25" width="50" height="50" rx="6" transform="translate(480,106) rotate(45)"/>
      </g>
      <rect x="329" y="47" width="20" height="28" rx="3" fill="#d8d8d6" role="img" aria-label="Keramik-Abutment"/>
      <rect x="423" y="40" width="18" height="30" rx="3" fill="#a9a9ab" role="img" aria-label="Titan-Abutment"/>
      <rect x="517" y="47" width="18" height="28" rx="3" fill="#e6dccd" role="img" aria-label="Zahnkrone"/>
      <rect x="377" y="92" width="20" height="28" rx="3" fill="#b4b4b6" role="img" aria-label="Titanbasis"/>
      <rect x="470" y="92" width="20" height="28" rx="3" fill="#c8b07e" role="img" aria-label="Goldfarbenes Abutment"/>
    </svg>
    <ul class="contact">
      <li class="c1"><svg width="12" height="12" viewBox="0 0 24 24"><path fill="#fff" d="M6.6 10.8a15 15 0 0 0 6.6 6.6l2.2-2.2c.3-.3.7-.4 1-.2 1.1.4 2.3.6 3.6.6.6 0 1 .4 1 1V20c0 .6-.4 1-1 1A17 17 0 0 1 3 4c0-.6.4-1 1-1h3.5c.6 0 1 .4 1 1 0 1.3.2 2.5.6 3.6.1.3 0 .7-.2 1z"/></svg>0221-5550140</li>
      <li class="c2"><svg width="12" height="12" viewBox="0 0 24 24"><path fill="#fff" d="M6 2h12v6H6zM4 9h16a2 2 0 0 1 2 2v6h-4v5H6v-5H2v-6a2 2 0 0 1 2-2zm4 8v3h8v-3z"/></svg>0221-555014-21</li>
      <li class="c3"><svg width="12" height="12" viewBox="0 0 24 24"><g fill="none" stroke="#fff" stroke-width="2"><circle cx="12" cy="12" r="9"/><path d="M3 12h18M12 3c3 3 3 15 0 18M12 3c-3 3-3 15 0 18"/></g></svg>www.dentaform.de</li>
    </ul>
    <div class="year">2019</div>
    <div class="brand"><span class="brand-dot"></span><span class="brand-name">DENTAFORM</span></div>
  </header>

  <nav class="month-bar">
    <span style="left:38px">Januar</span><span style="left:119px">Februar</span><span style="left:201px">März</span><span style="left:283px">April</span><span style="left:365px">Mai</span><span style="left:448px">Juni</span><span style="left:530px">Juli</span><span style="left:612px">August</span><span style="left:694px">September</span><span style="left:776px">Oktober</span><span style="left:858px">November</span><span style="left:940px">Dezember</span><span style="left:1037px">Januar 2020</span>
  </nav>

  <section class="months">
    <div class="month"><ol>
      <li class="h"><b>01</b><s>Di</s><i>Neujahr</i></li><li><b>02</b><s>Mi</s></li><li><b>03</b><s>Do</s></li><li><b>04</b><s>Fr</s></li><li class="h"><b>05</b><s>Sa</s></li><li class="h"><b>06</b><s>So</s><i>Heilige Drei Könige*</i></li><li><b>07</b><s>Mo</s></li><li><b>08</b><s>Di</s></li><li><b>09</b><s>Mi</s></li><li><b>10</b><s>Do</s></li><li><b>11</b><s>Fr</s></li><li class="h"><b>12</b><s>Sa</s></li><li class="h"><b>13</b><s>So</s></li><li><b>14</b><s>Mo</s></li><li><b>15</b><s>Di</s></li><li><b>16</b><s>Mi</s></li><li><b>17</b><s>Do</s></li><li><b>18</b><s>Fr</s></li><li class="h"><b>19</b><s>Sa</s></li><li class="h"><b>20</b><s>So</s></li><li><b>21</b><s>Mo</s></li><li><b>22</b><s>Di</s></li><li><b>23</b><s>Mi</s></li><li><b>24</b><s>Do</s></li><li><b>25</b><s>Fr</s></li><li class="h"><b>26</b><s>Sa</s></li><li class="h"><b>27</b><s>So</s></li><li><b>28</b><s>Mo</s></li><li><b>29</b><s>Di</s></li><li><b>30</b><s>Mi</s></li><li><b>31</b><s>Do</s></li>
    </ol><p class="foot">*Heilige Drei Könige: BW, BY, ST</p></div>

    <div class="month"><ol>
      <li><b>01</b><s>Fr</s></li><li class="h"><b>02</b><s>Sa</s></li><li class="h"><b>03</b><s>So</s></li><li><b>04</b><s>Mo</s></li><li><b>05</b><s>Di</s></li><li><b>06</b><s>Mi</s></li><li><b>07</b><s>Do</s></li><li><b>08</b><s>Fr</s></li><li class="h"><b>09</b><s>Sa</s></li><li class="h"><b>10</b><s>So</s></li><li><b>11</b><s>Mo</s></li><li><b>12</b><s>Di</s></li><li><b>13</b><s>Mi</s></li><li><b>14</b><s>Do</s><i>Valentinstag</i></li><li><b>15</b><s>Fr</s></li><li class="h"><b>16</b><s>Sa</s></li><li class="h"><b>17</b><s>So</s></li><li><b>18</b><s>Mo</s></li><li><b>19</b><s>Di</s></li><li><b>20</b><s>Mi</s></li><li><b>21</b><s>Do</s></li><li><b>22</b><s>Fr</s></li><li class="h"><b>23</b><s>Sa</s></li><li class="h"><b>24</b><s>So</s></li><li><b>25</b><s>Mo</s></li><li><b>26</b><s>Di</s></li><li><b>27</b><s>Mi</s></li><li><b>28</b><s>Do</s></li>
    </ol></div>

    <div class="month"><ol>
      <li><b>01</b><s>Fr</s></li><li class="h"><b>02</b><s>Sa</s></li><li class="h"><b>03</b><s>So</s></li><li><b>04</b><s>Mo</s><i>Rosenmontag</i></li><li><b>05</b><s>Di</s><i>Fastnacht</i></li><li><b>06</b><s>Mi</s><i>Ascher-mittwoch</i></li><li><b>07</b><s>Do</s></li><li><b>08</b><s>Fr</s></li><li class="h"><b>09</b><s>Sa</s></li><li class="h"><b>10</b><s>So</s></li><li><b>11</b><s>Mo</s></li><li><b>12</b><s>Di</s></li><li><b>13</b><s>Mi</s></li><li><b>14</b><s>Do</s></li><li><b>15</b><s>Fr</s></li><li class="h"><b>16</b><s>Sa</s></li><li class="h"><b>17</b><s>So</s></li><li><b>18</b><s>Mo</s></li><li><b>19</b><s>Di</s></li><li><b>20</b><s>Mi</s></li><li><b>21</b><s>Do</s></li><li><b>22</b><s>Fr</s></li><li class="h"><b>23</b><s>Sa</s></li><li class="h"><b>24</b><s>So</s></li><li><b>25</b><s>Mo</s></li><li><b>26</b><s>Di</s></li><li><b>27</b><s>Mi</s></li><li><b>28</b><s>Do</s></li><li><b>29</b><s>Fr</s></li><li class="h"><b>30</b><s>Sa</s></li><li class="h"><b>31</b><s>So</s><i>Beginn der Sommerzeit</i></li>
    </ol></div>

    <div class="month"><ol>
      <li><b>01</b><s>Mo</s></li><li><b>02</b><s>Di</s></li><li><b>03</b><s>Mi</s></li><li><b>04</b><s>Do</s></li><li><b>05</b><s>Fr</s></li><li class="h"><b>06</b><s>Sa</s></li><li class="h"><b>07</b><s>So</s></li><li><b>08</b><s>Mo</s></li><li><b>09</b><s>Di</s></li><li><b>10</b><s>Mi</s></li><li><b>11</b><s>Do</s></li><li><b>12</b><s>Fr</s></li><li class="h"><b>13</b><s>Sa</s></li><li class="h"><b>14</b><s>So</s><i>Palmsonntag</i></li><li><b>15</b><s>Mo</s></li><li><b>16</b><s>Di</s></li><li><b>17</b><s>Mi</s></li><li><b>18</b><s>Do</s><i>Grün-donnerstag</i></li><li class="h"><b>19</b><s>Fr</s><i>Karfreitag</i></li><li class="h"><b>20</b><s>Sa</s><i>Karsamstag</i></li><li class="h"><b>21</b><s>So</s><i>Ostersonntag</i></li><li class="h"><b>22</b><s>Mo</s><i>Ostermontag</i></li><li><b>23</b><s>Di</s></li><li><b>24</b><s>Mi</s></li><li><b>25</b><s>Do</s></li><li><b>26</b><s>Fr</s></li><li class="h"><b>27</b><s>Sa</s></li><li class="h"><b>28</b><s>So</s></li><li><b>29</b><s>Mo</s></li><li><b>30</b><s>Di</s><i>Walpurgis-nacht</i></li>
    </ol></div>

    <div class="month"><ol>
      <li class="h"><b>01</b><s>Mi</s><i>Tag der Arbeit</i></li><li><b>02</b><s>Do</s></li><li><b>03</b><s>Fr</s></li><li class="h"><b>04</b><s>Sa</s></li><li class="h"><b>05</b><s>So</s></li><li><b>06</b><s>Mo</s></li><li><b>07</b><s>Di</s></li><li><b>08</b><s>Mi</s></li><li><b>09</b><s>Do</s></li><li><b>10</b><s>Fr</s></li><li class="h"><b>11</b><s>Sa</s></li><li class="h"><b>12</b><s>So</s><i>Muttertag</i></li><li><b>13</b><s>Mo</s></li><li><b>14</b><s>Di</s></li><li><b>15</b><s>Mi</s></li><li><b>16</b><s>Do</s></li><li><b>17</b><s>Fr</s></li><li class="h"><b>18</b><s>Sa</s></li><li class="h"><b>19</b><s>So</s></li><li><b>20</b><s>Mo</s></li><li><b>21</b><s>Di</s></li><li><b>22</b><s>Mi</s></li><li><b>23</b><s>Do</s></li><li><b>24</b><s>Fr</s></li><li class="h"><b>25</b><s>Sa</s></li><li class="h"><b>26</b><s>So</s></li><li><b>27</b><s>Mo</s></li><li><b>28</b><s>Di</s></li><li><b>29</b><s>Mi</s></li><li class="h"><b>30</b><s>Do</s><i>Christi Himmelfahrt</i></li><li><b>31</b><s>Fr</s></li>
    </ol></div>

    <div class="month"><ol>
      <li class="h"><b>01</b><s>Sa</s></li><li class="h"><b>02</b><s>So</s></li><li><b>03</b><s>Mo</s></li><li><b>04</b><s>Di</s></li><li><b>05</b><s>Mi</s></li><li><b>06</b><s>Do</s></li><li><b>07</b><s>Fr</s></li><li class="h"><b>08</b><s>Sa</s></li><li class="h"><b>09</b><s>So</s><i>Pfingst-sonntag</i></li><li class="h"><b>10</b><s>Mo</s><i>Pfingst-montag</i></li><li><b>11</b><s>Di</s></li><li><b>12</b><s>Mi</s></li><li><b>13</b><s>Do</s></li><li><b>14</b><s>Fr</s></li><li class="h"><b>15</b><s>Sa</s></li><li class="h"><b>16</b><s>So</s></li><li><b>17</b><s>Mo</s></li><li><b>18</b><s>Di</s></li><li><b>19</b><s>Mi</s></li><li class="h"><b>20</b><s>Do</s><i>Fronleichnam*</i></li><li><b>21</b><s>Fr</s></li><li class="h"><b>22</b><s>Sa</s></li><li class="h"><b>23</b><s>So</s></li><li><b>24</b><s>Mo</s><i>Johannistag</i></li><li><b>25</b><s>Di</s></li><li><b>26</b><s>Mi</s></li><li><b>27</b><s>Do</s></li><li><b>28</b><s>Fr</s></li><li class="h"><b>29</b><s>Sa</s><i>Peter und Paul</i></li><li class="h"><b>30</b><s>So</s></li>
    </ol><p class="foot">*Fronleichnam: BW, BY, HE, NW, RP, SL</p></div>

    <div class="month"><ol>
      <li><b>01</b><s>Mo</s></li><li><b>02</b><s>Di</s></li><li><b>03</b><s>Mi</s></li><li><b>04</b><s>Do</s></li><li><b>05</b><s>Fr</s></li><li class="h"><b>06</b><s>Sa</s></li><li class="h"><b>07</b><s>So</s></li><li><b>08</b><s>Mo</s></li><li><b>09</b><s>Di</s></li><li><b>10</b><s>Mi</s></li><li><b>11</b><s>Do</s></li><li><b>12</b><s>Fr</s></li><li class="h"><b>13</b><s>Sa</s></li><li class="h"><b>14</b><s>So</s></li><li><b>15</b><s>Mo</s></li><li><b>16</b><s>Di</s></li><li><b>17</b><s>Mi</s></li><li><b>18</b><s>Do</s></li><li><b>19</b><s>Fr</s></li><li class="h"><b>20</b><s>Sa</s></li><li class="h"><b>21</b><s>So</s></li><li><b>22</b><s>Mo</s></li><li><b>23</b><s>Di</s></li><li><b>24</b><s>Mi</s></li><li><b>25</b><s>Do</s></li><li><b>26</b><s>Fr</s></li><li class="h"><b>27</b><s>Sa</s></li><li class="h"><b>28</b><s>So</s></li><li><b>29</b><s>Mo</s></li><li><b>30</b><s>Di</s></li><li><b>31</b><s>Mi</s></li>
    </ol></div>

    <div class="month"><ol>
      <li><b>01</b><s>Do</s></li><li><b>02</b><s>Fr</s></li><li class="h"><b>03</b><s>Sa</s></li><li class="h"><b>04</b><s>So</s></li><li><b>05</b><s>Mo</s></li><li><b>06</b><s>Di</s></li><li><b>07</b><s>Mi</s></li><li><b>08</b><s>Do</s></li><li><b>09</b><s>Fr</s></li><li class="h"><b>10</b><s>Sa</s></li><li class="h"><b>11</b><s>So</s></li><li><b>12</b><s>Mo</s></li><li><b>13</b><s>Di</s></li><li><b>14</b><s>Mi</s></li><li class="h"><b>15</b><s>Do</s><i>Mariä Himmelfahrt*</i></li><li><b>16</b><s>Fr</s></li><li class="h"><b>17</b><s>Sa</s></li><li class="h"><b>18</b><s>So</s></li><li><b>19</b><s>Mo</s></li><li><b>20</b><s>Di</s></li><li><b>21</b><s>Mi</s></li><li><b>22</b><s>Do</s></li><li><b>23</b><s>Fr</s></li><li class="h"><b>24</b><s>Sa</s></li><li class="h"><b>25</b><s>So</s></li><li><b>26</b><s>Mo</s></li><li><b>27</b><s>Di</s></li><li><b>28</b><s>Mi</s></li><li><b>29</b><s>Do</s></li><li><b>30</b><s>Fr</s></li><li class="h"><b>31</b><s>Sa</s></li>
    </ol><p class="foot">*Mariä Himmelfahrt: BY, SL</p></div>

    <div class="month"><ol>
      <li class="h"><b>01</b><s>So</s></li><li><b>02</b><s>Mo</s></li><li><b>03</b><s>Di</s></li><li><b>04</b><s>Mi</s></li><li><b>05</b><s>Do</s></li><li><b>06</b><s>Fr</s></li><li class="h"><b>07</b><s>Sa</s></li><li class="h"><b>08</b><s>So</s></li><li><b>09</b><s>Mo</s></li><li><b>10</b><s>Di</s></li><li><b>11</b><s>Mi</s></li><li><b>12</b><s>Do</s></li><li><b>13</b><s>Fr</s></li><li class="h"><b>14</b><s>Sa</s></li><li class="h"><b>15</b><s>So</s></li><li><b>16</b><s>Mo</s></li><li><b>17</b><s>Di</s></li><li><b>18</b><s>Mi</s></li><li><b>19</b><s>Do</s></li><li><b>20</b><s>Fr</s></li><li class="h"><b>21</b><s>Sa</s></li><li class="h"><b>22</b><s>So</s></li><li><b>23</b><s>Mo</s></li><li><b>24</b><s>Di</s></li><li><b>25</b><s>Mi</s></li><li><b>26</b><s>Do</s></li><li><b>27</b><s>Fr</s></li><li class="h"><b>28</b><s>Sa</s></li><li class="h"><b>29</b><s>So</s></li><li><b>30</b><s>Mo</s></li>
    </ol></div>

    <div class="month"><ol>
      <li><b>01</b><s>Di</s></li><li><b>02</b><s>Mi</s></li><li class="h"><b>03</b><s>Do</s><i>Tag der Deutschen Einheit</i></li><li><b>04</b><s>Fr</s></li><li class="h"><b>05</b><s>Sa</s></li><li class="h"><b>06</b><s>So</s><i>Erntedankfest</i></li><li><b>07</b><s>Mo</s></li><li><b>08</b><s>Di</s></li><li><b>09</b><s>Mi</s></li><li><b>10</b><s>Do</s></li><li><b>11</b><s>Fr</s></li><li class="h"><b>12</b><s>Sa</s></li><li class="h"><b>13</b><s>So</s></li><li><b>14</b><s>Mo</s></li><li><b>15</b><s>Di</s></li><li><b>16</b><s>Mi</s></li><li><b>17</b><s>Do</s></li><li><b>18</b><s>Fr</s></li><li class="h"><b>19</b><s>Sa</s></li><li class="h"><b>20</b><s>So</s></li><li><b>21</b><s>Mo</s></li><li><b>22</b><s>Di</s></li><li><b>23</b><s>Mi</s></li><li><b>24</b><s>Do</s></li><li><b>25</b><s>Fr</s></li><li class="h"><b>26</b><s>Sa</s></li><li class="h"><b>27</b><s>So</s><i>Ende der Sommerzeit</i></li><li><b>28</b><s>Mo</s></li><li><b>29</b><s>Di</s></li><li><b>30</b><s>Mi</s></li><li class="h"><b>31</b><s>Do</s><i>Reformations-tag*</i></li>
    </ol><p class="foot">*Reformationstag:<br>BB, HH, MV, NI, SH, SN, ST, TH</p></div>

    <div class="month"><ol>
      <li class="h"><b>01</b><s>Fr</s><i>Allerheiligen*</i></li><li class="h"><b>02</b><s>Sa</s><i>Allerseelen</i></li><li class="h"><b>03</b><s>So</s></li><li><b>04</b><s>Mo</s></li><li><b>05</b><s>Di</s></li><li><b>06</b><s>Mi</s></li><li><b>07</b><s>Do</s></li><li><b>08</b><s>Fr</s></li><li class="h"><b>09</b><s>Sa</s></li><li class="h"><b>10</b><s>So</s></li><li><b>11</b><s>Mo</s><i>St. Martin</i></li><li><b>12</b><s>Di</s></li><li><b>13</b><s>Mi</s></li><li><b>14</b><s>Do</s></li><li><b>15</b><s>Fr</s></li><li class="h"><b>16</b><s>Sa</s></li><li class="h"><b>17</b><s>So</s><i>Volks-trauertag</i></li><li><b>18</b><s>Mo</s></li><li><b>19</b><s>Di</s></li><li class="h"><b>20</b><s>Mi</s><i>Buß- und Bettag*</i></li><li><b>21</b><s>Do</s></li><li><b>22</b><s>Fr</s></li><li class="h"><b>23</b><s>Sa</s></li><li class="h"><b>24</b><s>So</s><i>Totensonntag</i></li><li><b>25</b><s>Mo</s></li><li><b>26</b><s>Di</s></li><li class="h"><b>27</b><s>Mi</s></li><li><b>28</b><s>Do</s></li><li><b>29</b><s>Fr</s></li><li class="h"><b>30</b><s>Sa</s></li>
    </ol><p class="foot">*Allerheiligen: BW, BY, NW, RP, SL<br>*Buß- und Bettag: SN</p></div>

    <div class="month"><ol>
      <li class="h"><b>01</b><s>So</s><i>1. Advent</i></li><li><b>02</b><s>Mo</s></li><li><b>03</b><s>Di</s></li><li><b>04</b><s>Mi</s></li><li><b>05</b><s>Do</s></li><li><b>06</b><s>Fr</s><i>Nikolaus</i></li><li class="h"><b>07</b><s>Sa</s></li><li class="h"><b>08</b><s>So</s><i>2. Advent</i></li><li><b>09</b><s>Mo</s></li><li><b>10</b><s>Di</s></li><li><b>11</b><s>Mi</s></li><li><b>12</b><s>Do</s></li><li><b>13</b><s>Fr</s></li><li class="h"><b>14</b><s>Sa</s></li><li class="h"><b>15</b><s>So</s><i>3. Advent</i></li><li><b>16</b><s>Mo</s></li><li><b>17</b><s>Di</s></li><li><b>18</b><s>Mi</s></li><li><b>19</b><s>Do</s></li><li><b>20</b><s>Fr</s></li><li class="h"><b>21</b><s>Sa</s></li><li class="h"><b>22</b><s>So</s><i>4. Advent</i></li><li><b>23</b><s>Mo</s></li><li><b>24</b><s>Di</s><i>Heiligabend</i></li><li class="h"><b>25</b><s>Mi</s><i>1. Weihnachts-feiertag</i></li><li class="h"><b>26</b><s>Do</s><i>2. Weihnachts-feiertag</i></li><li class="h"><b>27</b><s>Fr</s><i>Norvak GmbH Urlaub</i></li><li class="h"><b>28</b><s>Sa</s></li><li class="h"><b>29</b><s>So</s></li><li class="h"><b>30</b><s>Mo</s><i>Norvak GmbH Urlaub</i></li><li class="h"><b>31</b><s>Di</s><i>Norvak GmbH Urlaub</i></li>
    </ol></div>

    <div class="month" style="margin-left:14px"><ol>
      <li class="h"><b>01</b><s>Mi</s><i>Neujahr</i></li><li><b>02</b><s>Do</s></li><li><b>03</b><s>Fr</s></li><li class="h"><b>04</b><s>Sa</s></li><li class="h"><b>05</b><s>So</s></li><li class="h"><b>06</b><s>Mo</s><i>Heilige Drei Könige*</i></li><li><b>07</b><s>Di</s></li><li><b>08</b><s>Mi</s></li><li><b>09</b><s>Do</s></li><li><b>10</b><s>Fr</s></li><li class="h"><b>11</b><s>Sa</s></li><li class="h"><b>12</b><s>So</s></li><li><b>13</b><s>Mo</s></li><li><b>14</b><s>Di</s></li><li><b>15</b><s>Mi</s></li><li><b>16</b><s>Do</s></li><li><b>17</b><s>Fr</s></li><li class="h"><b>18</b><s>Sa</s></li><li class="h"><b>19</b><s>So</s></li><li><b>20</b><s>Mo</s></li><li><b>21</b><s>Di</s></li><li><b>22</b><s>Mi</s></li><li><b>23</b><s>Do</s></li><li><b>24</b><s>Fr</s></li><li class="h"><b>25</b><s>Sa</s></li><li class="h"><b>26</b><s>So</s></li><li><b>27</b><s>Mo</s></li><li><b>28</b><s>Di</s></li><li><b>29</b><s>Mi</s></li><li><b>30</b><s>Do</s></li><li><b>31</b><s>Fr</s></li>
    </ol><p class="foot">*Heilige Drei Könige: BW, BY, ST</p></div>
  </section>

  <div class="bottom-strip"></div>
</div>
</body>
</html>
```